Business Card + Letterhead Design for KESTOVA TRADING INC.

We already have a logo; now we need a business card + letterhead. We import and distribute flags and souvenirs with an emphasis on soccer related memorabilia. We target various ethnic markets and sporting goods stores. "International Souvenirs"

```html
<!DOCTYPE html>
<html lang="en">
<head>
<meta charset="utf-8">
<title>Kestova Trading – Stationery</title>
<link rel="stylesheet" href="https://fonts.googleapis.com/css2?family=Josefin+Sans:wght@400;600&family=Tinos&display=swap">
<style>
:root{
  --paper:#ffffff;
  --ink:#111111;
  --brand-red:#8c1c1c;
  --deep-red:#5e0d0d;
  --bright-red:#c01010;
  --ghost:#2c2c2c;
  --divider:#888888;
}
*{margin:0;padding:0;box-sizing:border-box}
html,body{width:1200px;height:1200px;overflow:hidden}
body{background:linear-gradient(90deg,#ececec 0%,#fafafa 60%,#dcdcdc 100%);font-family:"Josefin Sans",sans-serif;position:relative}

/* Shared wordmark */
.brand{position:absolute;display:flex;align-items:center;font-weight:600;white-space:nowrap}
.brand .dot{border-radius:50%;flex:none}
.brand .words{display:flex;flex-direction:column;line-height:1}
.brand .word-main{letter-spacing:1px}
.brand .word-sub{margin-top:3px}

/* Letterhead */
.letterhead{position:absolute;left:40px;top:113px;width:716px;height:1011px;background:var(--paper);box-shadow:0 2px 8px rgba(0,0,0,.12);overflow:hidden}
.letterhead .rule-left{position:absolute;left:0;top:22px;width:50px;height:4px;background:var(--ink)}
.letterhead .rule-right{position:absolute;left:233px;top:22px;width:227px;height:4px;background:var(--ink)}
.letterhead .rule-end{position:absolute;left:699px;top:22px;width:17px;height:4px;background:var(--ink)}
.letterhead .brand{left:56px;top:9px;gap:12px;color:var(--brand-red)}
.letterhead .brand .dot{width:28px;height:28px;background:var(--ink)}
.letterhead .brand .word-main{font-size:21px}
.letterhead .brand .word-sub{font-size:9px;letter-spacing:4.6px}
.letterhead .contact{position:absolute;left:469px;top:19px;width:228px;font-family:"Tinos",serif;font-size:9px;color:var(--brand-red);line-height:14px;white-space:nowrap}
.letterhead .contact .row{display:flex}
.letterhead .contact .row span{display:inline-flex;align-items:center;gap:6px;width:116px}
.letterhead .contact .row span + span{border-left:1px solid var(--ink);padding-left:6px;width:auto}
.icon{width:9px;height:9px;flex:none}
.letterhead .footer-swoosh{position:absolute;left:0;bottom:0;width:716px;height:170px}
.letterhead .footer-mark{position:absolute;left:563px;top:912px;width:96px;height:96px;border-radius:50%;border:16px solid var(--paper)}
.tagline{position:absolute;font-weight:400;white-space:nowrap}
.letterhead .tagline{left:296px;top:980px;font-size:16px;color:var(--paper)}

/* Business card front */
.card{position:absolute;overflow:hidden;box-shadow:0 2px 6px rgba(0,0,0,.2)}
.card-front{left:633px;top:285px;width:498px;height:272px;background:var(--ink);border:1px solid var(--bright-red);transform:rotate(-1.2deg)}
.card-front .top{position:absolute;inset:0}
.card-front .brand{left:30px;top:28px;gap:14px;color:var(--paper)}
.card-front .brand .dot{width:36px;height:36px;background:var(--ink);border:3px solid var(--paper)}
.card-front .brand .word-main{font-size:36px}
.card-front .brand .word-sub{font-size:14px;letter-spacing:9.5px}
.card-front .mark{position:absolute;left:340px;top:80px;width:150px;height:150px;border-radius:50%;border:24px solid var(--paper)}
.card-front .name-tag{position:absolute;left:10px;top:190px;width:130px;height:20px;background:var(--brand-red);border-radius:0 10px 10px 0;color:var(--paper);font-family:"Tinos",serif;font-size:11px;line-height:20px;padding-left:18px}
.card-front .contact{position:absolute;left:200px;top:160px;padding-left:22px;border-left:1px solid var(--divider);font-family:"Tinos",serif;font-size:10.5px;color:var(--paper);line-height:15px}
.card-front .contact div{display:flex;align-items:center;gap:10px}

/* Business card back */
.card-back{left:671px;top:549px;width:493px;height:278px;background:var(--ink)}
.card-back .top{position:absolute;inset:0}
.card-back .brand{left:10px;top:30px;gap:9px;color:var(--paper)}
.card-back .brand .dot{width:24px;height:24px;background:var(--ink);border:3px solid var(--paper)}
.card-back .brand .word-main{font-size:22px}
.card-back .brand .word-sub{font-size:9px;letter-spacing:5.6px}
.card-back .brand.ghost{left:196px;top:120px;gap:12px;color:var(--ghost)}
.card-back .brand.ghost .dot{width:34px;height:34px;background:transparent;border:4px solid var(--ghost)}
.card-back .brand.ghost .word-main{font-size:30px}
.card-back .brand.ghost .word-sub{font-size:12px;letter-spacing:7.6px}
.card-back .band{position:absolute;left:0;top:229px;width:100%;height:38px;background:var(--paper)}
.card-back .base{position:absolute;left:0;bottom:0;width:100%;height:11px;background:var(--ink)}
.card-back .web{position:absolute;left:10px;top:238px;display:flex;align-items:center;gap:8px;font-family:"Tinos",serif;font-size:10px;color:var(--ink)}
.card-back .web .dot{width:20px;height:20px;border-radius:50%;background:var(--ink)}
.card-back .tagline{left:182px;top:239px;font-size:17px;color:var(--brand-red)}
</style>
</head>
<body>

<section class="letterhead">
  <div class="rule-left"></div>
  <div class="brand"><span class="dot"></span><span class="words"><span class="word-main">KESTOVA</span><span class="word-sub">TRADING</span></span></div>
  <div class="rule-right"></div>
  <div class="contact">
    <div>2207-48 Maple Ridge Rd. Toronto, ON, Canada M4K 2P8</div>
    <div class="row">
      <span><svg class="icon" viewBox="0 0 10 10"><path d="M1 3h8v5H1z M3 1h4v2H3z" fill="#111"/></svg>(647) 555-0182</span>
      <span><svg class="icon" viewBox="0 0 10 10"><rect x="1" y="2" width="8" height="7" fill="none" stroke="#111"/><rect x="3" y="4" width="4" height="2" fill="#111"/></svg>(866) 555-0147</span>
    </div>
    <div class="row">
      <span><svg class="icon" viewBox="0 0 10 10"><rect x="1" y="2" width="8" height="6" fill="none" stroke="#111"/><path d="M1 2l4 3 4-3" fill="none" stroke="#111"/></svg>sales@kestovatrading.ca</span>
      <span><svg class="icon" viewBox="0 0 10 10"><rect x="1" y="1" width="8" height="8" fill="#111"/><rect x="2" y="3" width="6" height="4" fill="#fff"/></svg>www.kestovatrading.ca</span>
    </div>
  </div>
  <div class="rule-end"></div>
  <svg class="footer-swoosh" viewBox="0 0 716 170" preserveAspectRatio="none">
    <path d="M716 0 C560 110 260 150 0 170 L716 170 Z" fill="#111"/>
  </svg>
  <div class="footer-mark"></div>
  <div class="tagline">international flags &amp; souvenire</div>
</section>

<section class="card card-front">
  <svg class="top" viewBox="0 0 498 272" preserveAspectRatio="none">
    <path d="M0 0H498V70C380 60 210 70 0 120Z" fill="#5e0d0d"/>
  </svg>
  <div class="brand"><span class="dot"></span><span class="words"><span class="word-main">KESTOVA</span><span class="word-sub">TRADING</span></span></div>
  <div class="mark"></div>
  <div class="name-tag">Daniel Moreau</div>
  <div class="contact">
    <div><svg class="icon" viewBox="0 0 10 10"><path d="M1 3h8v5H1z M3 1h4v2H3z" fill="#fff"/></svg>(647) 555-0182</div>
    <div><svg class="icon" viewBox="0 0 10 10"><rect x="1" y="2" width="8" height="7" fill="none" stroke="#fff"/></svg>(866) 555-0147</div>
    <div><svg class="icon" viewBox="0 0 10 10"><rect x="1" y="2" width="8" height="6" fill="none" stroke="#fff"/><path d="M1 2l4 3 4-3" fill="none" stroke="#fff"/></svg>sales@kestovatrading.ca</div>
    <div><svg class="icon" viewBox="0 0 10 10"><rect x="1" y="1" width="8" height="8" fill="#fff"/></svg>www.kestovatrading.ca</div>
  </div>
</section>

<section class="card card-back">
  <svg class="top" viewBox="0 0 493 278" preserveAspectRatio="none">
    <defs>
      <radialGradient id="redGlow" cx="0.45" cy="0.1" r="0.7">
        <stop offset="0" stop-color="#c01010"/>
        <stop offset="1" stop-color="#5a0a0a"/>
      </radialGradient>
    </defs>
    <path d="M0 0H493V70C330 70 150 100 0 165Z" fill="url(#redGlow)"/>
  </svg>
  <div class="brand"><span class="dot"></span><span class="words"><span class="word-main">KESTOVA</span><span class="word-sub">TRADING</span></span></div>
  <div class="brand ghost"><span class="dot"></span><span class="words"><span class="word-main">KESTOVA</span><span class="word-sub">TRADING</span></span></div>
  <div class="band"></div>
  <div class="base"></div>
  <div class="web"><span class="dot"></span>www.kestovatrading.ca</div>
  <div class="tagline">international flags &amp; souvenire</div>
</section>

</body>
</html>
```